Homes, Invest in Non-performing loans

We need only 3 web pages, one for the home, one for the content, one for the properties.
The main focus of our business is to offer non performing loans (before foreclosures) to the general public. All the non-performing mortgages will end in a house, an apartment, a store, etc.
Our customers are able to invest from 10,000usd to 1,000,000usd (average 50,000usd).
Our customers' usual focus groups are employees who want second earnings, perceiving the business feeling without outlay time. They look for a solid finance sense corporation that confers them certainty.
Nearly all our clients desire the house, apartment, store, etc. more than the actual earnings.
The name of our company is BRAMLEY
Reason: We value the time and effort you already invest in our project. We realize that we did't come back on some of the doubts requested by the designers. It will be inequitable to the designers who prerequisite our feedback. We also appreciate the comprehension of the community in this postponement.
Reason: Designers,
We really apreciate all the time and effort you put on our project. From the begining we ask for 3 pages, so now we will leave the 10 finalist and provide some extra time to submit the other 2 pages.
We will race the price in 10%
Target Market(s)
Our customers average investors works as employees and want to have a second income or business without spending time. (People from 35 to 50)
Industry/Entity Type
Finance
Requirements
Should not have
- FLASH

```html
<!DOCTYPE html>
<html lang="en">
<head>
<meta charset="utf-8">
<title>BRAMLEY — Homes, Invest in Non-performing Loans</title>
<link href="https://fonts.googleapis.com/css2?family=Open+Sans:ital,wght@0,400;0,600;0,700;1,400&family=EB+Garamond:ital@1&family=Arimo:wght@400;700&display=swap" rel="stylesheet">
<style>
:root{
  --olive:#7f7f22;
  --olive-dark:#5e5e14;
  --olive-text:#7a7a1e;
  --orange:#e97f05;
  --blue:#0b76d6;
  --charcoal:#242424;
  --slate:#454545;
  --page-dark:#121212;
  --panel:#ffffff;
  --tile:#e6e6e6;
  --tile-border:#d6d6d6;
  --ink:#333333;
  --muted:#8a8a8a;
}
*{box-sizing:border-box;margin:0;padding:0}
html,body{width:1181px;height:1200px;overflow:hidden}
body{background:var(--page-dark);font-family:"Arimo",Arial,sans-serif;color:var(--ink)}
.site{position:absolute;left:0;top:0;width:1100px;height:1118px;transform:scale(1.0736,1.0733);transform-origin:0 0;
  background:repeating-linear-gradient(45deg,#141414 0 2px,#0e0e0e 2px 4px)}
.abs{position:absolute}

/* top utility bar */
.utility-bar{left:0;top:0;width:1100px;height:30px;background:linear-gradient(#85852a,#6b6b1c 60%,#2d2d10)}
.utility-btn{top:5px;height:20px;background:#1c2a17;color:#e6e6e6;font:400 13px/20px "Open Sans",sans-serif;text-align:center;border-radius:2px}
.utility-btn.register{left:850px;width:105px}
.utility-btn.login{left:970px;width:65px}

/* header */
.header{left:0;top:30px;width:1100px;height:123px;background:#fff}
.brand{left:88px;top:62px;display:flex;align-items:center;gap:8px;font:700 30px/1 "Open Sans",sans-serif;color:var(--charcoal);letter-spacing:1px}
.brand-mark{width:18px;height:18px;background:var(--olive)}
.social{top:63px;width:34px;height:34px;border-radius:50%;background:radial-gradient(circle at 35% 30%,#7fd0f0,#1e8ec4)}
.social.one{left:903px}.social.two{left:948px;background:radial-gradient(circle at 35% 30%,#a8e4f7,#38a9d8)}
.social.three{left:991px;background:radial-gradient(circle at 35% 30%,#6c8fd8,#2a4f9e)}
.main-nav{left:357px;top:104px;width:680px;height:40px;display:flex;background:var(--charcoal);border-radius:0 3px 3px 0}
.main-nav a{color:#fff;text-decoration:none;font:600 14px/40px "Open Sans",sans-serif;text-align:center;border-right:1px solid #3a3a3a}
.main-nav a.active{background:var(--olive)}

/* content panel */
.panel{left:71px;top:153px;width:965px;height:880px;background:var(--panel)}
.hero{left:82px;top:165px;width:944px;height:285px;background:linear-gradient(180deg,#4f6f33 0%,#7d9a57 30%,#c9d1d3 45%,#dfe3e4 65%,#5f7b3e 85%,#6f8a45 100%)}
.tagline{left:134px;top:195px;width:834px;height:83px;background:rgba(255,255,255,.55);text-align:center;font:italic 44px/83px "EB Garamond",serif;color:#666}

/* feature cards */
.feature{top:475px;width:281px;height:138px;border-radius:7px;overflow:hidden;color:#fff}
.feature.orange{left:102px;background:var(--orange)}
.feature.olive{left:411px;background:var(--olive)}
.feature.blue{left:718px;background:var(--blue)}
.feature h2{margin:12px 10px 0 14px;padding-bottom:7px;font:600 16px/1.3 "Open Sans",sans-serif;border-bottom:1px dashed rgba(255,255,255,.55)}
.feature p{margin:8px 50px 0 15px;font:12px/1.2 Arial,sans-serif}
.feature .corner{position:absolute;right:0;bottom:0}

/* guide tiles */
.guide{width:282px;height:53px;background:var(--tile);border:1px solid var(--tile-border);border-radius:2px}
.guide svg{position:absolute;left:6px;top:5px}
.guide a{position:absolute;top:3px;color:var(--olive-text);font:700 13px/1.2 "Open Sans",sans-serif;text-decoration:underline;letter-spacing:.3px}
.guide p{position:absolute;top:21px;font:11.5px/1.15 "Open Sans",sans-serif;color:#333}

/* signup */
.signup{left:717px;top:639px;width:283px;height:212px;background:#ebebeb;border:1px solid #d8d8d8;border-radius:8px}
.signup h3{position:absolute;left:13px;top:14px;width:257px;padding-bottom:8px;border-bottom:1px dashed #c0c0c0;font:600 15px/1.3 "Open Sans",sans-serif;color:var(--olive-text)}
.field{position:absolute;left:11px;width:256px;height:31px;background:linear-gradient(#fafafa,#efefef);border:1px solid #d9d9d9;border-radius:5px;font:13px/29px "Open Sans",sans-serif;color:#444;padding-left:9px}
.subscribe{position:absolute;left:11px;top:171px;width:95px;height:27px;border-radius:4px;background:linear-gradient(#86862a,#5f5f16);color:#fff;font:700 13px/27px "Open Sans",sans-serif;text-align:center}

/* news */
.news{left:102px;top:876px;width:898px;height:133px;background:#4a4a4a;border-radius:3px}
.news-tab{position:absolute;left:0;top:0}
.news-title{position:absolute;left:17px;top:10px;font:italic 19px/1.2 "Open Sans",sans-serif;color:#fff}
.news p{position:absolute;left:19px;top:52px;width:670px;font:12px/18px Arial,sans-serif;color:#fff}
.news-photo{position:absolute;left:696px;top:9px;width:189px;height:112px;border-radius:3px;background:linear-gradient(160deg,#f4f4f4 0%,#cfd8e2 45%,#8aa0b8 60%,#c9ceb8 80%,#e8e8e0 100%)}

/* footer */
.footer-links{left:0;top:1048px;width:1100px;text-align:center;font:12px/18px Arial,sans-serif;color:var(--muted)}
.footer-links span{margin:0 4px}
.footer-bar{left:0;top:1083px;width:1100px;height:35px;background:var(--slate);text-align:center;color:#ddd;font:12px/35px Arial,sans-serif}
</style>
</head>
<body>
<div class="site">
  <div class="abs utility-bar"></div>
  <div class="abs utility-btn register">Register</div>
  <div class="abs utility-btn login">Login</div>

  <header class="abs header"></header>
  <div class="abs brand"><span class="brand-mark"></span>BRAMLEY</div>
  <span class="abs social one"></span>
  <span class="abs social two"></span>
  <span class="abs social three"></span>
  <nav class="abs main-nav">
    <a class="active" style="width:80px">HOME</a>
    <a style="width:107px">ABOUT US</a>
    <a style="width:111px">BUY NOTES</a>
    <a style="width:142px">REOS FOR SALE</a>
    <a style="width:121px">SELL NOTES</a>
    <a style="width:119px;border-right:0">CONTACT US</a>
  </nav>

  <main class="abs panel"></main>
  <div class="abs hero" role="img" aria-label="Photo of a white two-storey family house with a front porch among green trees"></div>
  <div class="abs tagline">Your tag line will come here</div>

  <section class="abs feature orange">
    <h2>FEATURED PROPERTY</h2>
    <p>Lorem Ipsum is simply dummy text of the printing and typesetting industry. Lorem Ipsum has been the industry's standard dummy text ever since the 1500s,</p>
    <svg class="corner" width="85" height="85" viewBox="0 0 85 85"><path d="M85 0V85H0Z" fill="#3b3b3b"/><circle cx="58" cy="60" r="16" fill="#fff"/><path d="M55 52l8 8-8 8" fill="none" stroke="#333" stroke-width="3"/></svg>
  </section>
  <section class="abs feature olive">
    <h2>FEATURED PROPERTY 2</h2>
    <p>Lorem Ipsum is simply dummy text of the printing and typesetting industry. Lorem Ipsum has been the industry's standard dummy text ever since the 1500s,</p>
    <svg class="corner" width="85" height="85" viewBox="0 0 85 85"><path d="M85 0V85H0Z" fill="#3b3b3b"/><circle cx="58" cy="60" r="16" fill="#fff"/><path d="M55 52l8 8-8 8" fill="none" stroke="#333" stroke-width="3"/></svg>
  </section>
  <section class="abs feature blue">
    <h2>FEATURED LOAN</h2>
    <p>Lorem Ipsum is simply dummy text of the printing and typesetting industry. Lorem Ipsum has been the industry's standard dummy text ever since the 1500s,</p>
    <svg class="corner" width="85" height="85" viewBox="0 0 85 85"><path d="M85 0V85H0Z" fill="#3b3b3b"/><circle cx="58" cy="60" r="16" fill="#fff"/><path d="M55 52l8 8-8 8" fill="none" stroke="#333" stroke-width="3"/></svg>
  </section>

  <div class="abs guide" style="left:101px;top:638px">
    <svg width="46" height="40" viewBox="0 0 46 40"><path d="M3 20L23 3l20 17" fill="none" stroke="#333" stroke-width="4"/><path d="M10 18v18h10V26h6v10h10V18L23 7z" fill="#333"/></svg>
    <a style="left:57px">Free Mortgage Guide</a><p style="left:58px">40-page print/PDF 1st-time buyers'<br>MoneySaving booklet</p>
  </div>
  <div class="abs guide" style="left:408px;top:638px">
    <svg width="46" height="44" viewBox="0 0 46 44" role="img" aria-label="Calculator icon"><rect x="6" y="4" width="34" height="36" rx="6" fill="#f08a1c" transform="rotate(-15 23 22)"/><circle cx="18" cy="18" r="4" fill="#fff"/><circle cx="29" cy="16" r="4" fill="#fff"/><circle cx="20" cy="29" r="4" fill="#fff"/><circle cx="31" cy="27" r="4" fill="#fff"/></svg>
    <a style="left:63px">Free Mortgage Guide</a><p style="left:62px">40-page print/PDF 1st-time buyers'<br>MoneySaving booklet</p>
  </div>
  <div class="abs guide" style="left:101px;top:719px">
    <svg width="46" height="42" viewBox="0 0 46 42" role="img" aria-label="Key icon"><circle cx="34" cy="10" r="8" fill="#b8bcc0"/><path d="M28 16L8 36l4 4 4-4-3-3 4-4 3 3 12-13" fill="#a6aaae"/></svg>
    <a style="left:57px">Free Mortgage Guide</a><p style="left:58px">40-page print/PDF 1st-time buyers'<br>MoneySaving booklet</p>
  </div>
  <div class="abs guide" style="left:408px;top:721px">
    <svg width="46" height="46" viewBox="0 0 46 46"><rect x="13" y="2" width="20" height="42" rx="4" fill="#eee" stroke="#666" stroke-width="1.5"/><rect x="16" y="7" width="14" height="11" fill="#9fb0a0"/><g fill="#777"><rect x="16" y="22" width="4" height="3"/><rect x="21" y="22" width="4" height="3"/><rect x="26" y="22" width="4" height="3"/><rect x="16" y="28" width="4" height="3"/><rect x="21" y="28" width="4" height="3"/><rect x="26" y="28" width="4" height="3"/><rect x="16" y="34" width="4" height="3"/><rect x="21" y="34" width="4" height="3"/><rect x="26" y="34" width="4" height="3"/></g></svg>
    <a style="left:51px">Free Mortgage Guide</a><p style="left:51px">40-page print/PDF 1st-time buyers'<br>MoneySaving booklet</p>
  </div>
  <div class="abs guide" style="left:101px;top:798px">
    <svg width="64" height="42" viewBox="0 0 64 42" role="img" aria-label="Stack of banknotes icon"><rect x="4" y="12" width="54" height="22" rx="3" fill="#d9dcc6" transform="rotate(12 31 23)"/><rect x="38" y="12" width="6" height="26" fill="#c0392b" transform="rotate(12 31 23)"/></svg>
    <a style="left:75px">Free Mortgage Guide</a><p style="left:75px">40-page print/PDF 1st-time buyers'<br>MoneySaving booklet</p>
  </div>
  <div class="abs guide" style="left:408px;top:797px">
    <svg width="46" height="46" viewBox="0 0 46 46" role="img" aria-label="Wallet icon"><rect x="6" y="6" width="26" height="8" fill="#5a9a3a"/><rect x="3" y="10" width="38" height="30" rx="4" fill="#7a4a1e"/><circle cx="40" cy="36" r="4" fill="#f3c215"/></svg>
    <a style="left:57px">Free Mortgage Guide</a><p style="left:58px">40-page print/PDF 1st-time buyers'<br>MoneySaving booklet</p>
  </div>

  <aside class="abs signup">
    <h3>SIGN UP TODAY!</h3>
    <div class="field" style="top:50px">Email Address:</div>
    <div class="field" style="top:90px">First Name:</div>
    <div class="field" style="top:131px">Last Name:</div>
    <div class="subscribe">Subscribe</div>
  </aside>

  <section class="abs news">
    <svg class="news-tab" width="276" height="43" viewBox="0 0 276 43"><path d="M0 0H262L275 21 262 43H0Z" fill="#2f2f2f"/><path d="M0 0H257L270 21 257 43H0Z" fill="url(#tabGrad)"/><defs><linearGradient id="tabGrad" x1="0" x2="1"><stop offset="0" stop-color="#6c6c1c"/><stop offset="1" stop-color="#939335"/></linearGradient></defs></svg>
    <h2 class="news-title">Mortgage News This Week</h2>
    <p>setindustry's standard dummy text ever since the 1500s,Lorem Ipsum is simply dummy text of the printing and typesetting industry. Lorem Ipsum has been the industry's standard dummy text ever since the 1500s, Lorem Ipsum is simply dummy text of the printing and typesetting industry. Lorem Ipsum has been the industry's standard dummy text ever since the 1500s,</p>
    <div class="news-photo" role="img" aria-label="Photo of a small model house standing on banknotes"></div>
  </section>

  <footer>
    <div class="abs footer-links">About us <span>|</span> Advertise with Homeward <span>|</span> Partners Press Room <span>|</span> Investor Relations <span>|</span> Free Content Center <span>|</span> Contact Us <span>|</span> Sitemap</div>
    <div class="abs footer-bar">© 2012 All Rights Reserved. &nbsp; Privacy Policy/ Terms of Use</div>
  </footer>
</div>
</body>
</html>
```